TIDE CREST MARINE Business card

Card for boat detailing business in Bermuda

Target Market(s)

clients. new clients

Industry/Entity Type

Marine

Contact Information for Business Card

TIDE CREST MARINE
Boat Maintenance & Detailing
Dorian K. Halloway
P: 441 972 4617
E: dhalloway@tidecrestmail.net
P.O. Box FL528
Fennick FLBX
Bermuda

Font styles to use
Sans Serif

Colors
85acd3
eaf1f7
0455a3
33b8a4
86cfc6
ffffff
cfdeed

Requirements
Must have
• ALL the information provided. Tropical, water, sky, blue/green/white elements.
Nice to have
• A silhoette of the boat in the photos provided.
Should not have
• Keep it simple and clean. Nothing over the top.

```html
<!DOCTYPE html>
<html lang="en">
<head>
<meta charset="utf-8">
<title>Tide Crest Marine – Business Card</title>
<link rel="stylesheet" href="https://fonts.googleapis.com/css2?family=Montserrat:wght@600&family=Lato:wght@400;700&display=swap">
<style>
  :root {
    --backdrop: #363636;
    --paper: #ffffff;
    --ocean: #0455a3;
    --lagoon: #33b8a4;
    --ink: #0b3563;
    --shadow: rgba(0, 0, 0, 0.6);
  }
  html, body {
    margin: 0;
    padding: 0;
    width: 1200px;
    height: 900px;
    overflow: hidden;
    background: var(--backdrop);
  }
  .stage {
    position: relative;
    width: 1200px;
    height: 900px;
  }
  .card {
    position: absolute;
    width: 477px;
    height: 294px;
    background: var(--paper);
    overflow: hidden;
    box-shadow: 4px 4px 6px var(--shadow);
  }
  .card-front {
    left: 120px;
    top: 275px;
    border-radius: 0 46px 0 46px;
  }
  .card-back {
    left: 619px;
    top: 276px;
    border-radius: 46px 0 46px 0;
  }
  .card-wave {
    position: absolute;
    inset: 0;
    width: 100%;
    height: 100%;
  }
  .card-wave path { fill: var(--ocean); }
  .company {
    position: absolute;
    left: 0;
    width: 100%;
    margin: 0;
    text-align: center;
    font-family: "Montserrat", sans-serif;
    font-weight: 600;
    font-size: 27px;
    letter-spacing: 0.3px;
    line-height: 1;
  }
  .card-front .company { top: 81px; color: var(--lagoon); }
  .card-back .company { top: 111px; color: var(--paper); }
  .person {
    position: absolute;
    top: 142px;
    left: 0;
    width: 100%;
    margin: 0;
    text-align: center;
    font-family: "Montserrat", sans-serif;
    font-weight: 600;
    font-size: 20px;
    line-height: 1;
    color: var(--ink);
  }
  .tagline {
    position: absolute;
    top: 162px;
    left: 0;
    width: 100%;
    margin: 0;
    text-align: center;
    font-family: "Lato", sans-serif;
    font-size: 14px;
    line-height: 1;
    color: var(--paper);
  }
  .contact, .address {
    position: absolute;
    top: 232px;
    margin: 0;
    font-family: "Lato", sans-serif;
    font-size: 14px;
    line-height: 17px;
    color: var(--paper);
  }
  .contact { left: 32px; }
  .contact b { font-weight: 700; }
  .address { right: 31px; text-align: right; font-style: normal; }
</style>
</head>
<body>
<main class="stage">
  <section class="card card-front" aria-label="Business card front">
    <svg class="card-wave" viewBox="0 0 477 294" aria-hidden="true">
      <path d="M0 146 Q250 258 477 153 L477 294 L0 294 Z"/>
    </svg>
    <h1 class="company">TIDE CREST MARINE</h1>
    <p class="person">Dorian K. Halloway</p>
    <p class="contact"><b>P:</b> 441 972 4617<br><b>E:</b> dhalloway@tidecrestmail.net</p>
    <address class="address">P.O. Box FL528 Fennick<br>FLBX Bermuda</address>
  </section>

  <section class="card card-back" aria-label="Business card back">
    <svg class="card-wave" viewBox="0 0 477 294" aria-hidden="true">
      <path d="M0 82 Q238 -24 477 80 L477 216 Q238 322 0 209 Z"/>
    </svg>
    <h2 class="company">TIDE CREST MARINE</h2>
    <p class="tagline">BOAT MAINTENANCE &amp; DETAILING</p>
  </section>
</main>
</body>
</html>
```